IT Company needs Website for new Web and Mobile products for Sports and Fitness

Background:

We developed web based white label frontend web solution, backend services and white label mobile apps for to log, analyze, share and control sport and fitness activities. The name of this product suite is "Trelvano" (http://trelvano-example.com)

This products will be used by customers that provide platforms and community systems for sport and fitness. One of the major USP's is, that our technology i open for nearly all common formats, devices and apps out in the market. This means, you can just upload your data directly from device, file or app - e.G. Brindle, Vextor, Kalppi, StrideNook, Jogmelda, BipBop and much others.

Two current concrete examples/References

(1) MyOrvane
It's an international platform from orvane for runners. It provides individual training lans and a training log. MyOrvane uses the Backend Product "Trelvano Hub" (see http://hub.trelvano-example.net for a landing page) to integrate device, file and app support. Before this, every user has to track his training with manual inputs

(2) Paceharbor and qel-zine
Both are German customers. Paceharor is focused on runners. qel-zine is focused on Triatheletes. Both use the Product "Trelvano Web". This is a complete web solution with web based frontend solutions for athletes and coaches.

What do we need?
We need website layout for B2B for our products. We don't need lot's of pages. We need the pretty and nice layout, so we can derive the pages we need.

IMPORTANT
We don't talk about the webpages for the product itself (this will be a different project in future). We talk about a website, explaining the products)
Updates

Hi all,

we just start reviewing the first designs, and try to give feedback as detailed as possible. We attached a PDF document, to describe the the products a little bit more detailed. 

As written in the description, in the end we have two different sections. One is the usual stuff like "start page", "about", "contact", "disclaimer", "pricing", "blah...." and one will be the Developer Section, the "Tec Section". This ist aimed to developers (of our customers) that will integrate our products in there existing system or which will integrate our services in there own software.  This "pages" are more like "documentation", so easy to read and cool to look at (cause developers likes it cool, but straight)

Dear all,

we just do the final review. Cause this week is with heavy load, it takes some time...

Cheers

Ulrik

Target Market(s)

* Platforms and Communities for sport, health and fitness
* Gyms

Industry/Entity Type

Concrete

Font styles to use
Sans Serif

Requirements
Must have
• * Templates shall base on bootstrap. If not, it shall be easily realized on our site with bootstrap or out of the box "full responsive"

* HTML5 / CSS3
Nice to have
• PAGES
- Start Page
- Generic Template (from which we can derive additional pages)
- Contact Page
- Disclaimer Page
- Blog/News Page
- "About us" Page (can be combined with disclaimer)
- One Example product page (in end we have 3 products), shall show (if you need product details, let me know)
- product and it's description
- pricing information
- Add-Ons for the product
- Developer Section Page (Start Point for developers, where the finde "basic technical concepts and developer API's
- Example Developer Page for technical concept
- Example Developer Page for API

LOGO ISSUE
You can use an align to the Logo attached OR provide a new logo. The given logo is a logo for our own B2C Website http://trelvano-example.net. It's not really necessary, that the logo or the color must be used for the product website. Maybe it will be better if it's a complete new one, to avoid irritation between Trelvano as a B2B product and trelvano-example.net as a B2C platform.
Should not have
• No Flash and other proprietary technologies

```html
<!DOCTYPE html>
<html lang="en">
<head>
<meta charset="utf-8">
<title>Trelvano – Contact</title>
<link rel="stylesheet" href="https://fonts.googleapis.com/css2?family=PT+Sans:ital,wght@0,400;0,700;1,400;1,700&family=PT+Sans+Narrow:wght@700&family=Signika:wght@400;600&display=swap">
<style>
:root{
  --orange:#e8860f;
  --orange-dark:#c96a05;
  --ink:#3a3a3a;
  --navy:#1f2d3d;
  --grey-text:#555;
  --panel-bg:#f4f4f4;
  --panel-line:#dcdcdc;
  --query-top:#5a5d61;
  --query-bottom:#2f3134;
  --footer:#232323;
}
*{box-sizing:border-box;margin:0;padding:0}
html,body{width:1200px;height:872px;overflow:hidden;background:#fff}
body{position:relative;font-family:"PT Sans",sans-serif;color:var(--ink)}
.abs{position:absolute}

/* header */
.brand{left:182px;top:12px;width:160px}
.brand-name{display:flex;align-items:center;gap:6px;font-family:"Signika",sans-serif;font-weight:600;font-size:30px;color:var(--orange);line-height:1}
.brand-mark{width:18px;height:18px;background:var(--orange);border-radius:50%}
.brand-tag{margin-top:14px;font-size:8px;font-weight:700;color:#222;letter-spacing:.1px;white-space:nowrap}
.nav{left:0;top:34px;width:1200px;height:24px}
.nav a{position:absolute;top:0;transform:translateX(-50%);font-size:11px;color:#555;text-decoration:none;line-height:24px;white-space:nowrap}
.nav .sep{position:absolute;top:0;width:1px;height:24px;background:#ddd}

/* hero */
.hero{left:0;top:99px;width:1200px;height:262px;background:
  radial-gradient(ellipse 260px 200px at 1010px 130px,#c8453c 0%,rgba(200,69,60,.5) 45%,rgba(200,69,60,0) 75%),
  linear-gradient(180deg,#f4d7a6 0%,#efb165 40%,#d98a4a 75%,#b86a45 100%)}
.hero-title{left:182px;top:142px;font-family:"Signika",sans-serif;font-weight:600;font-size:31px;line-height:40px;letter-spacing:.2px}
.hero-title .l1{color:var(--orange)}
.hero-title .l2{color:#3b3b3b}
.signup{left:180px;top:247px;width:383px;height:39px;background:#f7f7f7;border:1px solid #cfcfcf;border-radius:4px;box-shadow:0 0 0 2px rgba(255,255,255,.6)}
.signup-label{left:16px;top:0;line-height:37px;font-size:10.5px;color:#888;letter-spacing:.2px}
.signup-btn{left:248px;top:2px;width:133px;height:33px;border-radius:3px;background:linear-gradient(#f5a623,#d07a06);color:#fff;font-size:16px;text-align:center;line-height:33px}

/* contact heading */
.section-title{left:213px;top:380px;font-family:"PT Sans Narrow",sans-serif;font-weight:700;font-size:24px;color:var(--navy)}
.section-title span{color:var(--orange)}
.section-rule{left:214px;top:424px;width:412px;height:10px;background:radial-gradient(ellipse at center top,rgba(0,0,0,.08),rgba(0,0,0,0) 70%)}

/* query form */
.query{left:207px;top:480px;width:223px;height:261px;border-radius:8px;background:linear-gradient(var(--query-top),var(--query-bottom));border:1px solid #222;box-shadow:0 2px 3px rgba(0,0,0,.3)}
.query-head{left:10px;top:10px;width:200px;height:35px;border-bottom:1px solid #6b6e72}
.query-title{left:58px;top:4px;font-size:20px;font-weight:700;color:#fff;font-variant:small-caps}
.field{position:absolute;left:16px;width:189px;height:27px;background:#fff;border:1px solid #ccc;border-radius:2px;font-size:10px;font-style:italic;color:#888;padding:6px 13px}
.submit{left:128px;top:218px;width:76px;height:27px;border-radius:3px;background:linear-gradient(#4a4a4a,#0e0e0e);color:#fff;font-size:14px;font-style:italic;font-weight:700;text-align:center;line-height:27px}

/* contact card */
.card{left:465px;top:480px;width:515px;height:261px;background:var(--panel-bg);border:1px solid var(--panel-line);border-radius:10px}
.map{left:41px;top:22px;width:217px;height:216px;background:linear-gradient(135deg,#ece8e1,#e2ddd4);border:1px solid #ccc}
.info{left:307px;top:36px;font-size:11.5px;color:#333;line-height:20.5px}
.info h3{font-weight:400;font-size:17px;color:#444;margin-bottom:20px;line-height:22px}
.info p{margin-bottom:20.5px}

/* footer */
.footer{left:0;top:800px;width:1200px;height:72px;background:linear-gradient(#1e1e1e,#2e2e2e);border-top:1px dotted #aaa;box-shadow:0 -2px 0 #fff,0 -3px 0 #ccc}
.social{left:210px;top:21px;display:flex;gap:11px}
.social span{width:22px;height:22px;border-radius:2px}
.s1{background:#3b5998}.s2{background:#3fb8e8}.s3{background:#555}.s4{background:#f39c1f}.s5{background:#c4302b}.s6{background:#7c97ab}
.copy{right:229px;top:16px;text-align:right;font-size:11.5px;color:#ddd;line-height:20.5px}
</style>
</head>
<body>

<header>
  <div class="abs brand">
    <div class="brand-name"><span class="brand-mark"></span>Trelvano</div>
    <div class="brand-tag">DIGITAL SPORT AND FITNESS SERVICES</div>
  </div>
  <nav class="abs nav">
    <a style="left:448px">HOME</a><span class="sep" style="left:491px"></span>
    <a style="left:543px">TRELVANO</a><span class="sep" style="left:593px"></span>
    <a style="left:660px">FITNESS CLOUD</a><span class="sep" style="left:723px"></span>
    <a style="left:782px">REFERENCES</a><span class="sep" style="left:838px"></span>
    <a style="left:893px">PRODUCTS</a><span class="sep" style="left:948px"></span>
    <a style="left:998px">SERVICES</a>
  </nav>
</header>

<section class="abs hero" role="img" aria-label="Photo of a runner's red running shoes on a warm, sunlit track"></section>
<h1 class="abs hero-title"><span class="l1">DIE OFFENE SPORT- UND</span><br><span class="l2">FITNESSPLATFORM FUR JEDEN SPORT</span></h1>
<div class="abs signup">
  <span class="abs signup-label">WHAT'S YOUR EMAIL ADDRESS :</span>
  <span class="abs signup-btn">JOIN FOR FREE</span>
</div>

<h2 class="abs section-title">Contact <span>Us</span></h2>
<div class="abs section-rule"></div>

<form class="abs query">
  <div class="abs query-head">
    <svg class="abs" style="left:0;top:-2px" width="40" height="36" viewBox="0 0 40 36">
      <g transform="rotate(-12 20 18)">
        <rect x="4" y="8" width="32" height="22" rx="2" fill="#f2f2f2" stroke="#bbb"/>
        <path d="M4 10 L20 22 L36 10" fill="none" stroke="#bbb" stroke-width="1.5"/>
      </g>
    </svg>
    <span class="abs query-title">Query</span>
  </div>
  <div class="field" style="top:55px">Name</div>
  <div class="field" style="top:91px">Email</div>
  <div class="field" style="top:126px">Phone</div>
  <div class="field" style="top:161px;height:45px;padding-top:12px">Message</div>
  <div class="abs submit">SUBMIT</div>
</form>

<section class="abs card">
  <div class="abs map" role="img" aria-label="Street map showing the office location with a red pin"></div>
  <div class="abs info">
    <h3>Contact Us</h3>
    <p>#17 Corvel Lane,Lorem ipsum,<br>Loruem dollar sit amet.</p>
    <p>Phone: +41 555 0192 37<br>Tollfree: (008) 55501846</p>
    <p>E-mail: info@trelvano-example.com</p>
  </div>
</section>

<footer class="abs footer">
  <div class="abs social">
    <span class="s1" role="img" aria-label="Social link"></span>
    <span class="s2" role="img" aria-label="Social link"></span>
    <span class="s3" role="img" aria-label="Social link"></span>
    <span class="s4" role="img" aria-label="Feed link"></span>
    <span class="s5" role="img" aria-label="Video link"></span>
    <span class="s6" role="img" aria-label="Email link"></span>
  </div>
  <div class="abs copy">© 2013 trelvano-example.com, All rights reserved<br>X2</div>
</footer>

</body>
</html>
```